BrightMesa Business Card Contest

We are looking for a modern business card that catches attention and is unique. Attached is the brand guide and logo files. Please note that the back side (not the side with our name and info) with be UV raise printed, so have fun with the design there. We want to include Name, Title, Phone number, email, website.

Contact Information for Business Card

Please see project description

```html
<!DOCTYPE html>
<html lang="en">
<head>
<meta charset="utf-8">
<title>BrightMesa Business Card</title>
<link rel="stylesheet" href="https://fonts.googleapis.com/css2?family=Montserrat:ital,wght@0,300;0,400;0,600;0,700;1,300&display=swap">
<style>
  :root {
    --backdrop: #1a1a1c;
    --navy: #252b68;
    --navy-light: #3a3f78;
    --strip: #2b2d33;
    --ink: #2a2d36;
    --orange: #e8892a;
    --gold: #e2ab3e;
    --paper: #ffffff;
    --paper-shade: #e6e6e8;
    --card-w: 680px;
    --card-h: 388px;
  }
  * { box-sizing: border-box; margin: 0; padding: 0; }
  html, body { width: 1200px; height: 916px; overflow: hidden; }
  body {
    background: var(--backdrop);
    font-family: "Montserrat", sans-serif;
    display: flex;
    flex-direction: column;
    align-items: center;
    justify-content: center;
    gap: 44px;
  }
  .card {
    width: var(--card-w);
    height: var(--card-h);
    position: relative;
    overflow: hidden;
    box-shadow: 0 14px 30px rgba(0,0,0,.55);
  }

  /* Back side */
  .card-back {
    background: linear-gradient(135deg, var(--navy-light) 0%, var(--navy) 55%, #1f2562 100%);
    display: flex;
    align-items: center;
    justify-content: center;
    gap: 18px;
  }
  .card-back .mark-dot {
    width: 54px; height: 54px; border-radius: 50%;
    background: var(--paper);
  }
  .card-back .brand-name {
    color: var(--paper);
    font-weight: 600;
    font-size: 54px;
    letter-spacing: -0.5px;
  }

  /* Front side */
  .card-front {
    background: linear-gradient(180deg, var(--paper) 0%, var(--paper) 60%, var(--paper-shade) 100%);
  }
  .side-strip {
    position: absolute; left: 0; top: 0; bottom: 0;
    width: 86px;
    background: var(--strip);
  }
  .side-strip .accent-band {
    position: absolute; left: 0; right: 0;
    top: 246px; height: 38px;
    background: var(--orange);
  }
  .icon-column {
    position: absolute; left: 54px; top: 52px;
    display: flex; flex-direction: column; gap: 17px;
  }
  .icon-column svg { width: 30px; height: 30px; display: block; }
  .contact-list {
    position: absolute; left: 118px; top: 52px;
    list-style: none;
    display: flex; flex-direction: column; gap: 17px;
  }
  .contact-list li {
    height: 30px; line-height: 30px;
    font-size: 18px; font-weight: 300; font-style: italic;
    color: var(--ink);
    letter-spacing: .3px;
    white-space: nowrap;
  }
  .brand-lockup {
    position: absolute; right: 44px; top: 168px;
    display: flex; align-items: center; gap: 10px;
  }
  .brand-lockup .mark-dot {
    width: 28px; height: 28px; border-radius: 50%;
    background: var(--ink);
  }
  .brand-lockup .brand-name {
    font-size: 40px; font-weight: 600; color: var(--ink);
    letter-spacing: -0.5px;
    white-space: nowrap;
  }
  .person {
    position: absolute; left: 118px; top: 258px;
    color: var(--ink);
  }
  .person .full-name { font-size: 22px; letter-spacing: .3px; line-height: 1; white-space: nowrap; }
  .person .first { font-weight: 700; }
  .person .last { font-weight: 300; }
  .person .role { font-size: 14px; font-weight: 300; margin-top: 4px; letter-spacing: .5px; }
  .gold-bar {
    position: absolute; right: 26px; top: 290px;
    width: 290px; height: 36px;
    background: var(--gold);
  }
</style>
</head>
<body>

  <section class="card card-back" aria-label="Card back">
    <span class="mark-dot"></span>
    <span class="brand-name">BrightMesa</span>
  </section>

  <section class="card card-front" aria-label="Card front">
    <div class="side-strip"><div class="accent-band"></div></div>

    <div class="icon-column">
      <svg viewBox="0 0 30 30" aria-label="Email">
        <circle cx="15" cy="15" r="14" fill="var(--orange)"/>
        <rect x="8" y="10" width="14" height="10" fill="none" stroke="var(--strip)" stroke-width="1.8"/>
        <path d="M8 10 L15 16 L22 10" fill="none" stroke="var(--strip)" stroke-width="1.8"/>
      </svg>
      <svg viewBox="0 0 30 30" aria-label="Phone">
        <circle cx="15" cy="15" r="14" fill="var(--orange)"/>
        <path d="M10 8 l3 0 l1 4 l-2 1.5 q1.5 3.5 4.5 5 l1.5 -2 l4 1 l0 3 q-1 1.5 -3 1.5 q-9 -1 -10.5 -11 q0 -2 1.5 -3z" fill="var(--strip)"/>
      </svg>
      <svg viewBox="0 0 30 30" aria-label="Website">
        <circle cx="15" cy="15" r="14" fill="var(--orange)"/>
        <circle cx="15" cy="15" r="7.5" fill="none" stroke="var(--strip)" stroke-width="1.6"/>
        <ellipse cx="15" cy="15" rx="3.2" ry="7.5" fill="none" stroke="var(--strip)" stroke-width="1.4"/>
        <line x1="7.5" y1="15" x2="22.5" y2="15" stroke="var(--strip)" stroke-width="1.4"/>
      </svg>
    </div>

    <ul class="contact-list">
      <li>hello@brightmesa.com</li>
      <li>+00 987 654 321</li>
      <li>www.brightmesa.com</li>
    </ul>

    <div class="brand-lockup">
      <span class="mark-dot"></span>
      <span class="brand-name">BrightMesa</span>
    </div>

    <div class="person">
      <p class="full-name"><span class="first">DANIEL</span><span class="last">WHITCOMBE</span></p>
      <p class="role">OWNER</p>
    </div>

    <div class="gold-bar"></div>
  </section>

</body>
</html>
```